Construction company that specializes in roofing and siding

https://bayfieldroofworks.com/featured-projects/

https://www.quarrymeadowrenewalllc.com/#

https://www.tallpinehomecrafters.com/residential-siding-services/

Please model a website after these examples
I posted a doc that has some content to get you started. I will upload more content and photos as the site progresses.

Coded - Design and coding required

5+ page

```html
<!DOCTYPE html>
<html lang="en">
<head>
<meta charset="utf-8">
<title>Stoneward Construction – Roofing &amp; Siding</title>
<link rel="stylesheet" href="https://fonts.googleapis.com/css2?family=Barlow:wght@400;500;600;700&family=Michroma&display=swap">
<style>
:root{
  --c-900:#4d4d4e;
  --c-700:#717173;
  --c-500:#8b8b8d;
  --c-300:#b1b1b3;
  --c-100:#cbcbcd;
  --board:#d6d6d7;
  --paper:#ffffff;
  --mist:#f2f3f5;
  --ink:#3f3f41;
  --text:#6d6d70;
  --display:"Michroma",sans-serif;
  --body:"Barlow",sans-serif;
}
*{box-sizing:border-box;margin:0;padding:0}
html,body{width:1200px;height:3380px;overflow:hidden}
body{background:var(--board);font-family:var(--body);color:var(--text);position:relative}
.abs{position:absolute}

/* style guide */
.guide-logo{left:181px;top:116px;display:flex;align-items:center;gap:12px}
.mark-square{width:46px;height:46px;background:var(--c-700);border-radius:4px}
.wordmark{font-family:var(--body);font-weight:600;color:var(--c-700);line-height:1.05;text-transform:uppercase}
.guide-logo .wordmark{font-size:24px;letter-spacing:2px}
.guide-logo .wordmark small{display:block;font-size:14px;letter-spacing:3.6px;font-weight:600}
.guide-title{font-size:26px;color:var(--c-700);font-weight:500}
.font-sample-display{font-family:var(--display);font-size:15px;color:var(--c-900);font-weight:700}
.font-sample-body{font-size:17px;color:var(--c-700)}
.swatches{left:783px;top:146px;display:flex;gap:10px}
.swatch{width:40px;text-align:center}
.swatch i{display:block;width:40px;height:40px;border-radius:50%}
.swatch span{display:block;margin-top:10px;font-size:8px;color:var(--c-900);margin-left:-6px;margin-right:-6px}

/* site */
.site{left:206px;top:295px;width:792px;height:2972px;background:var(--paper);overflow:hidden}
.site > *{position:absolute}

.nav{left:0;top:0;width:792px;height:46px;background:#fff;border-bottom:1px solid #ececee}
.nav .logo{left:24px;top:9px;display:flex;align-items:center;gap:7px;position:absolute}
.nav .mark-square{width:26px;height:26px;border-radius:3px}
.nav .wordmark{font-size:12px;letter-spacing:1px}
.nav .wordmark small{display:block;font-size:7.5px;letter-spacing:1.6px}
.menu{position:absolute;left:254px;top:17px;display:flex;gap:0;font-size:8.5px;color:var(--c-700)}
.menu li{list-style:none;position:absolute;white-space:nowrap}
.menu li::after{content:"";display:inline-block;width:4px;height:4px;border-right:1px solid currentColor;border-bottom:1px solid currentColor;transform:rotate(45deg);margin-left:5px;position:relative;top:-2px}
.menu li.active{text-decoration:underline;color:var(--ink)}
.phone-btn{position:absolute;left:682px;top:9px;width:85px;height:28px;border:1px solid var(--c-700);border-radius:3px;display:flex;align-items:center;justify-content:center;gap:5px;font-size:7.5px;color:var(--ink);font-weight:500}
.dropdown{left:253px;top:48px;width:121px;height:66px;background:#fff;box-shadow:0 2px 8px rgba(0,0,0,.15);padding:10px 10px;font-size:7px;color:var(--c-700);z-index:3}
.dropdown li{list-style:none;margin-bottom:8px}
.dropdown li::before{content:"•";margin-right:5px;color:var(--c-500)}

.hero-photo{left:0;top:46px;width:792px;height:452px;background:linear-gradient(135deg,#4f4f51 0%,#6c6c6e 40%,#9a9a9c 70%,#cfcfd1 100%)}
.hero-shape{left:0;top:0;width:792px;height:500px}
.hero-bracket{left:89px;top:177px;width:26px;height:151px;border:2px solid #fff;border-right:none}
.hero-title{left:109px;top:199px;font-family:var(--display);color:#fff;line-height:1.25}
.hero-title .l1{font-size:33px;display:block;letter-spacing:1px}
.hero-title .l2{font-size:24.5px;display:block;letter-spacing:1px}
.hero-sub{left:109px;top:285px;font-size:11.5px;letter-spacing:1.4px;color:#fff}

.quote-form{left:476px;top:115px;width:211px;height:274px;background:rgba(246,246,247,.96);border:1px solid #e0e0e2;padding:18px 20px 0 21px}
.quote-form h2{font-size:13px;color:var(--ink);font-weight:500;margin-bottom:10px}
.field label{display:block;font-size:6.5px;color:var(--c-700);margin-bottom:4px}
.field div{height:22px;border:1px solid #d0d0d2;background:#efeff1;border-radius:2px;margin-bottom:9px}
.btn{display:inline-flex;align-items:center;justify-content:center;gap:5px;font-size:7px;font-weight:600;border-radius:2px;height:27px}
.btn-dark{background:linear-gradient(#6a6a6c,#505052);color:#fff;box-shadow:0 2px 3px rgba(0,0,0,.25)}
.btn-line{border:1px solid var(--c-500);color:var(--c-700);background:#fff}
.btn-light{background:#fff;color:var(--ink)}
.quote-form .btn{width:80px;margin-top:6px}

.about-photo{left:24px;top:518px;width:354px;height:357px;background:radial-gradient(circle at 50% 50%,#9e9ea0 0%,#d7d7d9 45%,#fbfbfb 75%)}
.section-title{font-family:var(--display);color:var(--c-900);font-size:18px;letter-spacing:1px}
.about-title{left:421px;top:552px}
.copy{font-size:9.4px;line-height:14px;color:var(--text)}
.copy b{color:var(--ink);font-weight:600}
.about-p1{left:421px;top:586px;width:268px}
.about-p2{left:421px;top:670px;width:268px}
.about-rule{left:421px;top:728px;width:265px;height:1px;background:#dcdcde}
.about-quote{left:421px;top:749px;width:268px;font-size:11px;line-height:15px;color:var(--ink)}
.author{left:421px;top:802px;display:flex;align-items:center;gap:7px}
.avatar{width:28px;height:28px;border-radius:50%;background:linear-gradient(#c9c9cb,#77777a);border:2px solid #eee}
.author strong{display:block;font-size:8px;color:var(--ink);font-weight:600}
.author em{display:block;font-size:7px;color:var(--c-500)}

.services{left:0;top:885px;width:792px;height:475px;background:var(--mist)}
.centered{left:0;width:792px;text-align:center}
.service-photo{top:992px;height:218px}
.service-name{top:1229px;font-size:10.5px;color:var(--ink);font-weight:500}
.service-tags{top:1251px;font-size:7px;color:var(--c-700);display:flex;gap:14px;white-space:nowrap}
.service-tags span::before{content:"• "}
.service-btn{top:1280px;width:80px}

.cta{left:0;top:1363px;width:792px;height:285px;background:linear-gradient(100deg,#6e6e70 0%,#8b8b8d 50%,#9d9d9f 100%)}
.cta-title{left:106px;top:1405px;color:#fff;line-height:25px;font-size:18px}
.cta-copy{left:106px;top:1470px;width:272px;color:#eeeef0}
.cta-btn{left:106px;top:1564px;width:80px}
.cta-art{left:400px;top:1363px;width:392px;height:285px}

.proj-photo{width:283px;height:220px}
.proj-title{font-size:14px;color:var(--ink);font-weight:500}
.proj-copy{width:286px;font-size:8.2px;line-height:13px}
.proj-btn{width:80px}

.why-title{left:106px;top:2511px;font-size:18px;line-height:25px}
.why-item{display:flex;align-items:center;gap:9px;font-size:9px;line-height:14px;color:var(--c-500)}
.why-box{left:555px;top:2526px;width:131px;height:59px;background:#f0f1f3}

.footer-art{left:0;top:2700px;width:792px;height:272px}
.footer-logo{left:0;width:792px;top:2782px;display:flex;justify-content:center;align-items:center;gap:8px}
.footer-logo .mark-square{width:34px;height:34px;background:#fff}
.footer-logo .wordmark{color:#fff;font-size:15px;letter-spacing:1.5px}
.footer-logo .wordmark small{display:block;font-size:9px;letter-spacing:2.2px}
.footer-contacts{top:2846px;font-size:7.5px;color:#fff;font-weight:500;display:flex;justify-content:center;gap:12px;align-items:center}
.footer-contacts i{display:inline-block;width:14px;height:1px;background:#fff}
.socials{top:2883px;display:flex;justify-content:center;gap:6px}
.socials span{width:20px;height:20px;border-radius:50%;background:#fff}
.copyright{top:2915px;font-size:6.5px;color:#eeeef0}
</style>
</head>
<body>

<!-- brand guide -->
<div class="abs guide-logo">
  <span class="mark-square"></span>
  <div class="wordmark">Stoneward<small>Construction</small></div>
</div>
<div class="abs guide-title" style="left:513px;top:104px">Fonts:</div>
<div class="abs font-sample-display" style="left:513px;top:155px">ETHNOCENTRIC</div>
<div class="abs font-sample-body" style="left:513px;top:178px">Barlow</div>
<div class="abs guide-title" style="left:783px;top:104px">Colors:</div>
<div class="abs swatches">
  <div class="swatch"><i style="background:var(--c-900)"></i><span>#4d4d4e</span></div>
  <div class="swatch"><i style="background:var(--c-700)"></i><span>#717173</span></div>
  <div class="swatch"><i style="background:var(--c-500)"></i><span>#8b8b8d</span></div>
  <div class="swatch"><i style="background:var(--c-300)"></i><span>#b1b1b3</span></div>
  <div class="swatch"><i style="background:#ececed"></i><span>#cbcbcd</span></div>
</div>

<main class="abs site">

  <!-- hero -->
  <div class="hero-photo" role="img" aria-label="Gabled house roofs with dark shingles against the sky"></div>
  <svg class="hero-shape" viewBox="0 0 792 500" aria-hidden="true">
    <polygon points="0,419 396,478 792,419 792,500 0,500" fill="#fff"/>
    <polygon points="80,440 396,480 736,436 396,498" fill="#6f6f71"/>
    <polygon points="0,419 396,474 792,419 792,430 396,480 0,430" fill="#fff"/>
  </svg>

  <header class="nav">
    <div class="logo"><span class="mark-square"></span><div class="wordmark">Stoneward<small>Construction</small></div></div>
    <ul class="menu">
      <li class="active" style="left:0">Roofing</li>
      <li style="left:61px">Siding</li>
      <li style="left:116px">Gutters</li>
      <li style="left:176px">Windows</li>
      <li style="left:242px">Storm Damage Repair</li>
    </ul>
    <div class="phone-btn">
      <svg width="8" height="8" viewBox="0 0 24 24"><path d="M6.6 10.8a15 15 0 0 0 6.6 6.6l2.2-2.2c.3-.3.7-.4 1-.2 1.1.4 2.3.6 3.6.6.6 0 1 .4 1 1V20c0 .6-.4 1-1 1C10.6 21 3 13.4 3 4c0-.6.4-1 1-1h3.5c.6 0 1 .4 1 1 0 1.3.2 2.5.6 3.6.1.3 0 .7-.2 1z" fill="#3f3f41"/></svg>
      +1 555 010 4400
    </div>
  </header>
  <ul class="dropdown">
    <li>Architectural shingles</li>
    <li>Standing Seam Steel Roofing</li>
    <li>Agriculture Steel Roofing</li>
  </ul>

  <div class="hero-bracket"></div>
  <h1 class="hero-title"><span class="l1">STONEWARD</span><span class="l2">CONSTRUCTION</span></h1>
  <p class="hero-sub">– your source for roofing and siding in Minnesota</p>

  <form class="quote-form">
    <h2>Request a Free Quote Below</h2>
    <div class="field"><label>Full Name*</label><div></div></div>
    <div class="field"><label>Phone Number*</label><div></div></div>
    <div class="field"><label>Email Address*</label><div></div></div>
    <div class="field"><label>Type of Service*</label><div></div></div>
    <span class="btn btn-dark">Send My Request</span>
  </form>

  <!-- about -->
  <div class="about-photo" role="img" aria-label="Roofer in a hard hat installing metal roof panels"></div>
  <h2 class="section-title about-title">ABOUT STONEWARD</h2>
  <p class="copy about-p1">In 2016 Dale Hartley started helping people with their home improvement projects. His very first job was installing window trim for a wonderful homeowner in Forest Lake MN. He did his best work and made sure he treated his first customer like family. After all, his first customer was June Hartley, his Mom.</p>
  <p class="copy about-p2">Today, Dale and the Stoneward Construction team are <b>helping homeowners around Minnesota</b>: carrying the spirit of his first job onto every job they touch.</p>
  <div class="about-rule"></div>
  <p class="about-quote">“We are helping a lot more people now, but we haven’t lost the dedication to service and craftsmanship that I had on my very first job.”</p>
  <div class="author">
    <span class="avatar" role="img" aria-label="Portrait of the owner"></span>
    <div><strong>- Dale Hartley, Owner</strong><em>Stoneward Construction</em></div>
  </div>

  <!-- services -->
  <section class="services"></section>
  <h2 class="section-title centered" style="top:936px">WHAT WE DO</h2>
  <div class="service-photo" style="left:0;width:91px;background:linear-gradient(160deg,#a9a9ab,#6b6b6d)" role="img" aria-label="House corner with gutter and downspout"></div>
  <div class="service-photo" style="left:106px;width:283px;background:linear-gradient(170deg,#b9b9bb 0%,#8e8e90 35%,#4a4a4c 100%)" role="img" aria-label="Standing seam steel roof under a cloudy sky"></div>
  <div class="service-photo" style="left:403px;width:283px;background:linear-gradient(90deg,#7b7b7d,#9a9a9c 60%,#d8d8da 72%,#8a8a8c 80%)" role="img" aria-label="Horizontal lap siding with white trim"></div>
  <div class="service-photo" style="left:701px;width:91px;background:linear-gradient(160deg,#8e8e90,#5d5d5f)" role="img" aria-label="Gutter on a house eave"></div>
  <div class="service-name" style="left:106px">Roofing</div>
  <div class="service-tags" style="left:106px"><span>Architectural shingles</span><span>Standing Steel Roofing</span><span>Agricultural Roofing</span></div>
  <span class="btn btn-dark service-btn" style="left:106px">Discover More →</span>
  <div class="service-name" style="left:403px">Siding</div>
  <div class="service-tags" style="left:403px;gap:9px"><span>Vinyl Siding</span><span>Fibercore Lap</span><span>Ridgeline Steel Siding</span><span>Northgrain Board Siding</span></div>
  <span class="btn btn-line service-btn" style="left:403px">Discover More →</span>
  <div class="service-name" style="left:701px">Gutters</div>
  <span class="btn btn-line service-btn" style="left:701px">Discover More →</span>

  <!-- call to action -->
  <section class="cta"></section>
  <h2 class="section-title cta-title" style="color:#fff">START TODAY -<br>GET A FREE QUOTE</h2>
  <div class="copy cta-copy">
    <p>For expert renovation, storm damage repair, or ongoing maintenance of your multi-family or residential property, the Stoneward Construction is your trusted partner.</p>
    <p style="margin-top:5px">Get started today by scheduling your free inspection quote and design consultations</p>
  </div>
  <span class="btn btn-light cta-btn">Get a Free Quote</span>
  <svg class="cta-art" viewBox="0 0 392 285" role="img" aria-label="Contractor with a tablet inspecting a new steel roof">
    <defs><linearGradient id="ctaPhoto" x1="0" y1="0" x2="1" y2="1"><stop offset="0" stop-color="#c9c9cb"/><stop offset=".5" stop-color="#6f6f71"/><stop offset="1" stop-color="#3f3f41"/></linearGradient></defs>
    <polygon points="135,0 392,0 392,285 102,285 14,142" fill="url(#ctaPhoto)"/>
    <polyline points="120,0 2,142 88,285" fill="none" stroke="#fff" stroke-width="3"/>
  </svg>

  <!-- projects -->
  <h2 class="section-title centered" style="top:1698px">FEATURED PROJECTS</h2>

  <div class="proj-photo" style="left:106px;top:1746px;background:linear-gradient(170deg,#bdbdbf,#7a7a7c 55%,#555557)" role="img" aria-label="Craftsman cottage with a new shingle roof"></div>
  <h3 class="proj-title" style="left:402px;top:1760px">Project &nbsp;1 Title Name Goes Here</h3>
  <div class="copy proj-copy" style="left:402px;top:1790px">
    <p>A charming cottage perched by Cedar Creek in Harrison, ME required a roof replacement. The owners had carefully researched their options and settled on the durable and stylish metal shingles from TerraGuard.</p>
    <p style="margin-top:10px">They contacted TerraGuard, the manufacturer, a local contractor recommendation. TerraGuard suggested Stoneward Construction, their preferred contractor in the region. Stoneward Construction, with their extensive experience and expertise, were well-equipped to handle.</p>
  </div>
  <span class="btn btn-line proj-btn" style="left:402px;top:1923px">Discover More →</span>

  <h3 class="proj-title" style="left:106px;top:2010px">Project &nbsp;2 Title Name Goes Here</h3>
  <div class="copy proj-copy" style="left:106px;top:2040px">
    <p>A charming cottage perched by Cedar Creek in Harrison, ME required a roof replacement. The owners had carefully researched their options and settled on the durable and stylish metal shingles from TerraGuard.</p>
    <p style="margin-top:10px">They contacted TerraGuard, the manufacturer, a local contractor recommendation. TerraGuard suggested Stoneward Construction, their preferred contractor in the region. Stoneward Construction, with their extensive experience and expertise, were well-equipped to handle.</p>
  </div>
  <span class="btn btn-dark proj-btn" style="left:106px;top:2172px">Discover More →</span>
  <div class="proj-photo" style="left:403px;top:1995px;background:linear-gradient(200deg,#e2e2e4,#8d8d8f 50%,#4b4b4d)" role="img" aria-label="Dormer window on a dark shingle roof beside a brick chimney"></div>

  <div class="proj-photo" style="left:106px;top:2244px;background:linear-gradient(180deg,#e4e4e6,#9b9b9d 55%,#5a5a5c)" role="img" aria-label="Roof eave with white gutter and downspout"></div>
  <h3 class="proj-title" style="left:402px;top:2258px">Project &nbsp;3 Title Name Goes Here</h3>
  <div class="copy proj-copy" style="left:402px;top:2288px">
    <p>A cute cabin nestled on Gull Lake in Nisswa, MN was in need of a new roof. The homeowners had already done their research and decided they wanted Corvane’s synthetic Spanish barrel tile.</p>
    <p style="margin-top:10px">They contacted TerraGuard, the manufacturer, a local contractor recommendation. TerraGuard suggested Stoneward Construction, their preferred contractor in the region. Stoneward Construction, with their extensive experience and expertise, were well-equipped to handle.</p>
  </div>
  <span class="btn btn-line proj-btn" style="left:402px;top:2421px">Discover More →</span>

  <!-- why us -->
  <h2 class="section-title why-title">WHY CHOOSE US<br>FOR ROOFING<br>AND SIDING?</h2>
  <div class="why-box"></div>
  <div class="why-item" style="left:421px;top:2540px">
    <svg width="30" height="26" viewBox="0 0 30 26" fill="none" stroke="#8b8b8d" stroke-width="1.4"><path d="M2 12 15 3l13 9M6 10v14h18V10M10 24v-8M14 24v-8M18 24v-8"/></svg>
    <span>Quality<br>Roofing</span>
  </div>
  <div class="why-item" style="left:574px;top:2540px">
    <svg width="28" height="28" viewBox="0 0 28 28" fill="none" stroke="#8b8b8d" stroke-width="1.4"><circle cx="14" cy="14" r="11"/><path d="m9 14 4 4 7-8"/></svg>
    <span>Experienced<br>Workers</span>
  </div>
  <div class="why-item" style="left:421px;top:2624px">
    <svg width="30" height="30" viewBox="0 0 30 30" fill="none" stroke="#8b8b8d" stroke-width="1.4"><path d="M24 3 14 15M8 14l8 8-6 5-7-7z"/></svg>
    <span>Afterwards<br>Cleanup</span>
  </div>
  <div class="why-item" style="left:574px;top:2624px">
    <svg width="30" height="28" viewBox="0 0 30 28" fill="none" stroke="#8b8b8d" stroke-width="1.3"><path d="m15 2 2.4 5 5.4.7-4 3.7 1 5.3-4.8-2.6-4.8 2.6 1-5.3-4-3.7 5.4-.7z"/><path d="M3 26c1-4 4-5 6-5M27 26c-1-4-4-5-6-5"/></svg>
    <span>Customer<br>Oriented</span>
  </div>

  <!-- footer -->
  <svg class="footer-art" viewBox="0 0 792 272" aria-hidden="true">
    <defs><linearGradient id="footGrad" x1="0" y1="0" x2="0" y2="1"><stop offset="0" stop-color="#6b6b6d"/><stop offset="1" stop-color="#8e8e90"/></linearGradient></defs>
    <polygon points="0,79 391,5 792,79 792,272 0,272" fill="url(#footGrad)"/>
    <polyline points="50,74 391,20 742,74" fill="none" stroke="#fff" stroke-width="3"/>
  </svg>
  <div class="footer-logo"><span class="mark-square"></span><div class="wordmark">Stoneward<small>Construction</small></div></div>
  <div class="footer-contacts centered">
    <span>inquiries@stonewardbuilds.com</span><i></i><span>+1 555 010 2200</span><i></i><span>Location, Street, Address goes here</span>
  </div>
  <div class="socials centered"><span></span><span></span><span></span></div>
  <div class="copyright centered">© 2024 Stoneward Construction</div>

</main>
</body>
</html>
```